Paws Haven

Need Yard signs
Dimensions 24" wide and 18" high

Copy: Rescue does not mean "Damaged". It means they have been let down by humans.
Please adopt at: 782 W Marlowe Ave, Tampa, Fl 33647
Open: Tues-Sun 10am - 7pm

I have attached a sample of the original ad. I can't use this because the resolution is too low and the type has to be big enough so that it can be seen 12 feet away.
I have also attached some photos you can use. The res may not be hi enough, but perhaps you can find some stock photography even these pics are not hi res enough.

Target Market(s)

animal lovers

Font styles to use
Sans Serif

Colors

Designer to choose colors to be used in the design.

Requirements
Must have
• Must be easy to read.

```html
<!DOCTYPE html>
<html lang="en">
<head>
<meta charset="utf-8">
<title>Paws Haven – Yard Sign</title>
<link href="https://fonts.googleapis.com/css2?family=Anton&family=Roboto:wght@700&family=Roboto+Condensed:wght@700&display=swap" rel="stylesheet">
<style>
  :root {
    --ink: #000000;
    --sun: #ffd800;
    --sun-shade: #c9a800;
    --paper: #ffffff;
    --photo-light: #b9c6c8;
    --photo-mid: #4f6468;
    --photo-dark: #141b1d;
  }
  html, body {
    margin: 0;
    padding: 0;
    width: 1200px;
    height: 900px;
    overflow: hidden;
    background: var(--ink);
  }
  .sign {
    position: relative;
    width: 1200px;
    height: 900px;
    background: var(--ink);
    overflow: hidden;
  }
  .sign__photo {
    position: absolute;
    left: 560px;
    top: 110px;
    width: 640px;
    height: 790px;
    background:
      radial-gradient(ellipse 45% 48% at 62% 48%, var(--photo-light) 0%, var(--photo-mid) 45%, var(--photo-dark) 80%, transparent 100%);
    -webkit-mask-image: linear-gradient(to right, transparent 0%, #000 30%);
            mask-image: linear-gradient(to right, transparent 0%, #000 30%);
  }
  .headline {
    position: absolute;
    left: 60px;
    top: 42px;
    margin: 0;
    font-family: "Roboto", sans-serif;
    font-weight: 700;
    font-size: 90px;
    line-height: 1;
    letter-spacing: 0.5px;
    color: var(--sun);
    white-space: nowrap;
  }
  .keyword {
    position: absolute;
    left: 36px;
    top: 150px;
    margin: 0;
    font-family: "Anton", sans-serif;
    font-size: 138px;
    line-height: 1;
    color: var(--sun);
    white-space: nowrap;
  }
  .keyword__quote {
    font-family: "Roboto", sans-serif;
    font-weight: 700;
    font-size: 96px;
    vertical-align: 38px;
  }
  .message {
    position: absolute;
    left: 68px;
    top: 308px;
    margin: 0;
    font-family: "Roboto Condensed", sans-serif;
    font-weight: 700;
    font-size: 42px;
    line-height: 52px;
    color: var(--paper);
  }
  .ribbon {
    position: absolute;
    left: 0;
    top: 0;
    width: 1200px;
    height: 900px;
  }
  .ribbon__label {
    position: absolute;
    left: 50px;
    top: 562px;
    margin: 0;
    font-family: "Anton", sans-serif;
    font-size: 62px;
    line-height: 1;
    color: var(--ink);
    white-space: nowrap;
  }
  .address {
    position: absolute;
    left: 46px;
    top: 664px;
    margin: 0;
    font-family: "Anton", sans-serif;
    font-size: 45px;
    line-height: 52px;
    color: var(--paper);
    font-style: normal;
  }
  .hours {
    position: absolute;
    left: 42px;
    top: 782px;
    margin: 0;
    font-family: "Roboto Condensed", sans-serif;
    font-weight: 700;
    font-size: 58px;
    line-height: 1;
    color: var(--sun);
    white-space: nowrap;
  }
</style>
</head>
<body>
<main class="sign">
  <div class="sign__photo" role="img" aria-label="Photo of a sad shelter dog behind a chain-link fence"></div>

  <h1 class="headline">RESCUE DOES NOT MEAN</h1>
  <p class="keyword"><span class="keyword__quote">“</span>DAMAGED.<span class="keyword__quote">”</span></p>

  <p class="message">IT MEANS THEY HAVE<br>BEEN LET DOWN<br>BY HUMANS.</p>

  <svg class="ribbon" viewBox="0 0 1200 900" aria-hidden="true">
    <polygon points="444,652 496,652 444,684" fill="var(--sun-shade)"/>
    <polygon points="26,538 452,538 496,652 26,652" fill="var(--sun)"/>
  </svg>
  <p class="ribbon__label">PLEASE ADOPT AT</p>

  <address class="address">782 W MARLOWE AVE,<br>TAMPA, FL 33647</address>

  <p class="hours">OPEN: TUES-SUN 10AM - 7PM</p>
</main>
</body>
</html>
```